New web design for a service provider in the medical field

We are looking for a new design for our website. We are a company that repairs and sells medical endoscopes. Our customers include doctors and hospitals. Our current website can be found at https://lumenfix.example/en/lumenfix-english.
We need a new web design (without programming) for the following 3 pages:
-Startpage https://lumenfix.example/en/lumenfix-english/
-Used endoscopes https://lumenfix.example/en/used-endoscopes/
-Purchase https://lumenfix.example/en/purchase/
The design should be modern and stylish.
The blue color of the logo should be reflected on the page, but not too intrusive.
I have uploaded the images from the header. If more images are needed, let me know and I will upload them.

Target Market(s)
Doctors and hospitals

```html
<!DOCTYPE html>
<html lang="en">
<head>
<meta charset="utf-8">
<title>LumenFix – Endoscope Repair and Sale</title>
<link rel="stylesheet" href="https://fonts.googleapis.com/css2?family=Rubik:wght@400;500;600;700&family=Roboto:wght@400;500;700&display=swap">
<style>
:root{
  --blue:#2a9fe0;
  --blue-dark:#1b7fc0;
  --navy:#0c1a25;
  --navy-2:#132634;
  --ink:#1f2b36;
  --muted:#6b7680;
  --light:#f4f8fb;
  --pale:#eaf6fd;
  --footer:#1d2227;
  --footer-2:#16191d;
  --white:#fff;
  --head:'Rubik',sans-serif;
  --body:'Roboto',sans-serif;
}
*{box-sizing:border-box;margin:0;padding:0}
html,body{width:1200px;height:4886px;overflow:hidden}
body{position:relative;font-family:var(--body);color:var(--ink);background:var(--white)}
section,header,footer{position:absolute;left:0;width:1200px;overflow:hidden}
.abs{position:absolute}
.center{left:0;width:100%;text-align:center}
.btn{position:absolute;display:flex;align-items:center;justify-content:center;border-radius:30px;font:600 14px var(--body);letter-spacing:.3px;text-transform:uppercase;background:var(--blue);color:var(--white)}
.btn-outline{background:transparent;border:2px solid var(--blue);color:var(--blue);font-size:11px}
.btn-outline.light{border-color:var(--blue);color:var(--blue)}

/* Header / hero */
.hero{top:0;height:720px;background:var(--navy)}
.hero-photo{position:absolute;inset:0;background:linear-gradient(120deg,#22313b 0%,#101d27 45%,#0b1822 100%)}
.hero-accent{position:absolute;inset:0}
.topbar{position:absolute;top:0;left:0;width:100%;height:30px;font:500 11px var(--body);color:#dfe7ee}
.topbar span{position:absolute;top:8px}
.nav{position:absolute;top:56px;left:0;width:100%;height:30px}
.brand{position:absolute;display:flex;align-items:center;gap:10px;font:600 18px var(--head);color:var(--white)}
.brand .dot{width:12px;height:12px;border-radius:50%;background:var(--blue)}
.nav a{position:absolute;top:8px;font:600 11px var(--body);color:var(--white);text-decoration:none}
.quote-btn{position:absolute;left:965px;top:48px;width:130px;height:37px;background:var(--blue);border-radius:3px;color:#fff;font:600 11px var(--body);display:flex;align-items:center;justify-content:center}
.hero-kicker{top:222px;font:500 15px var(--body);letter-spacing:3px;color:var(--blue)}
.hero-title{top:254px;font:600 58px/72px var(--head);color:var(--white)}
.hero-title em{font-style:normal;color:var(--blue)}
.hero-rule{position:absolute;top:363px;height:1px;background:rgba(255,255,255,.35)}
.hero-text{top:414px;left:330px;width:540px;text-align:center;font:400 13px/25px var(--body);color:#e5ecf1}
.slider-dots{position:absolute;left:1090px;top:310px;font:600 11px var(--body);color:#fff}
.slider-dots li{list-style:none;height:41px;width:30px;text-align:center}
.slider-dots li.on span{display:inline-block;width:34px;height:34px;margin-left:-2px;margin-top:-10px;border:2px solid #fff;border-radius:50%;line-height:30px}

.band{top:720px;height:143px;background:var(--white)}
.band-text{top:54px;left:0;width:1125px;text-align:center;font:500 28px var(--head);color:var(--white)}
.band-text em{font-style:normal;color:var(--blue)}

/* Services */
.services{top:863px;height:715px;background:var(--white)}
.section-title{font:500 38px var(--head);color:var(--ink)}
.brand-strip{position:absolute;top:125px;left:0;width:100%;height:144px;background:var(--pale)}
.brand-strip span{position:absolute;top:54px;font:700 34px var(--head);color:var(--ink);transform:translateX(-50%)}
.svc{position:absolute;top:350px;width:300px;text-align:center}
.svc h3{font:600 25px/26px var(--head);color:var(--blue-dark)}
.svc p{margin-top:36px;font:400 11.5px/20px var(--body);color:var(--muted)}

/* Faulty */
.faulty{top:1578px;height:338px;background:var(--navy)}
.faulty-photo{position:absolute;inset:0;background:linear-gradient(90deg,#0e1a23,#1d2b35 50%,#0e1a23)}
.faulty h2{top:78px;font:600 46px var(--head);color:#fff}
.faulty .sub{top:148px;font:600 23px var(--head);color:#fff}
.faulty .link{top:196px;font:500 18px var(--body);color:var(--blue)}

/* Why */
.why{top:1916px;height:578px;background:var(--light)}
.why-map{position:absolute;left:520px;top:120px;width:600px;height:320px;border-radius:40%;background:radial-gradient(ellipse at center,rgba(150,170,185,.22),rgba(150,170,185,0) 70%)}
.why h2{left:87px;top:84px;font:500 40px/48px var(--head);color:var(--ink)}
.why h2 em{display:block;font-style:normal;color:var(--blue)}
.feature{position:absolute;width:200px;height:68px;background:#fff;box-shadow:0 3px 10px rgba(0,0,0,.08);display:flex;align-items:center;justify-content:center;text-align:center;font:500 15px/18px var(--body);color:var(--ink)}
.why-logo{position:absolute;left:778px;top:260px;display:flex;align-items:center;gap:16px;font:500 44px var(--head);color:var(--navy-2)}
.why-logo .dot{width:26px;height:26px;border-radius:50%;background:var(--blue)}

/* Testimonials */
.testi{top:2494px;height:461px;background:var(--navy)}
.testi h2{top:44px;font:600 38px var(--head);color:#fff}
.card{position:absolute;left:247px;top:137px;width:678px;height:271px;background:#fff}
.card .name{position:absolute;left:82px;top:45px;font:500 14px var(--body);color:var(--ink)}
.card p{position:absolute;left:82px;top:80px;width:540px;font:400 12.5px/26px var(--body);color:#4a545d}
.card .more{position:absolute;left:84px;top:217px;font:600 11px var(--body);color:var(--blue);text-decoration:underline}
.card .mark{position:absolute;right:30px;top:170px;font:700 110px/1 Georgia,serif;color:#e3e7ea}
.avatar{position:absolute;left:188px;top:124px;width:124px;height:124px;border-radius:50%;border:5px solid #fff;background:linear-gradient(160deg,#c9d5de,#7f97a8);box-shadow:0 0 0 3px var(--blue)}

/* Decision */
.decision{top:2955px;height:785px;background:#f7f9fb}
.decision h2{top:62px;font:500 39px/52px var(--head);color:var(--navy-2)}
.benefit{position:absolute;width:280px;text-align:center}
.benefit svg{display:block;margin:0 auto}
.benefit h4{margin-top:12px;font:500 15.5px/17px var(--body);color:var(--ink)}
.benefit p{margin-top:8px;font:400 11.5px/22px var(--body);color:var(--muted)}

/* Help */
.help{top:3740px;height:518px;background:var(--navy)}
.help-photo{position:absolute;inset:0;background:linear-gradient(160deg,#3a5368,#1e3344 55%,#16293a)}
.help h2{top:160px;font:500 46px var(--head);color:#fff}

.contact-card{position:absolute;top:4154px;width:237px;height:231px;background:#fff;box-shadow:0 8px 24px rgba(0,0,0,.15);text-align:center;z-index:3}
.contact-card svg{display:block;margin:32px auto 0}
.contact-card h5{margin-top:14px;font:500 18px var(--body);color:var(--ink)}
.contact-card p{margin:10px auto 0;width:170px;font:400 12px/24px var(--body);color:var(--muted)}

/* Footer */
.footer{top:4258px;height:628px;background:var(--footer)}
.footer h6{position:absolute;top:252px;font:500 16px var(--body);color:#c8d0d6}
.footer ul{position:absolute;top:290px;list-style:none;font:400 12px/27.7px var(--body);color:#6c767e}
.footer .about{position:absolute;left:104px;top:310px;width:240px;font:400 11.5px/22px var(--body);color:#7d878f}
.socials{position:absolute;left:104px;top:410px;display:flex;gap:14px}
.socials i{width:11px;height:11px;border-radius:50%;background:#5f6a72}
.news-text{position:absolute;left:874px;top:288px;width:230px;font:400 11.5px/22px var(--body);color:#6c767e}
.news-input{position:absolute;left:874px;top:340px;width:232px;height:40px;background:#fff;display:flex;align-items:center}
.news-input span{padding-left:18px;font:400 12px var(--body);color:#666;flex:1}
.news-input b{width:42px;height:40px;background:var(--blue);display:flex;align-items:center;justify-content:center}
.bottom{position:absolute;left:0;top:542px;width:100%;height:86px;background:var(--footer-2);font:400 11.5px var(--body);color:#c5ccd2}
.bottom span{position:absolute;top:32px}
</style>
</head>
<body>

<header class="hero">
  <div class="hero-photo" role="img" aria-label="Photo of a flexible endoscope in a repair workshop"></div>
  <svg class="hero-accent" width="1200" height="720" viewBox="0 0 1200 720">
    <polygon points="1000,0 1200,0 1200,720 780,720" fill="#2a9fe0" opacity=".85"/>
    <polygon points="1060,0 1200,0 1200,400" fill="#4bb4ec" opacity=".5"/>
  </svg>

  <div class="topbar">
    <span style="left:92px">✉ info@lumenfix.example</span>
    <span style="left:278px">☏ +49 4000 555 210-0</span>
    <span style="left:697px">PICK-UP ORDER</span>
    <span style="left:820px">ABOUT US</span>
    <span style="left:913px">CONTACT US</span>
    <span style="left:1012px;display:flex;gap:20px;top:10px"><i style="width:9px;height:9px;border-radius:50%;background:#fff;display:block"></i><i style="width:9px;height:9px;border-radius:50%;background:#fff;display:block"></i><i style="width:9px;height:9px;border-radius:50%;background:#fff;display:block"></i><i style="width:9px;height:9px;border-radius:50%;background:#fff;display:block"></i></span>
  </div>

  <div class="brand" style="left:92px;top:60px"><span class="dot"></span>LumenFix</div>
  <nav class="nav">
    <a style="left:391px">Endoscope Repair</a>
    <a style="left:514px">Used Endoscopes</a>
    <a style="left:638px">Endoscopy Systems</a>
    <a style="left:791px">Accessories</a>
    <a style="left:885px">Catalog</a>
  </nav>
  <div class="quote-btn">GET A QUOTE</div>

  <div class="abs center hero-kicker">YOUR FUTURE - OUR SERVICE</div>
  <h1 class="abs center hero-title">Put Your <em>Endoscope</em> in<br>Relaible Hands !</h1>
  <div class="hero-rule" style="left:200px;width:168px"></div>
  <div class="hero-rule" style="left:835px;width:170px"></div>
  <p class="abs hero-text">LumenFix GmbH is specialised in the repair and sale of Meridan, Kestrel and Halvora flexible medical endoscopes. As a service-oriented company, we are at your side with our knowledge and skills!</p>
  <div class="btn btn-outline" style="left:525px;top:524px;width:149px;height:40px;color:#6fc1ef">LEARN MORE</div>

  <ul class="slider-dots">
    <li>01</li><li>02</li><li class="on"><span>03</span></li><li>04</li><li>05</li>
  </ul>
</header>

<section class="band">
  <div class="abs" role="img" aria-label="Close-up photo of endoscope equipment" style="inset:0;background:linear-gradient(90deg,#1c3140,#0f2433)"></div>
  <svg class="abs" style="left:0;top:0" width="1200" height="143" viewBox="0 0 1200 143">
    <polygon points="860,0 1200,0 1200,143 805,143" fill="#fff"/>
    <polygon points="780,0 860,0 805,143 740,143" fill="#0b2638"/>
  </svg>
  <div class="abs band-text">Your Future - <em>Our Service</em></div>
  <div class="btn btn-outline" style="left:905px;top:54px;width:148px;height:42px">CONTACT NOW</div>
</section>

<section class="services">
  <h2 class="abs center section-title" style="top:47px">Our Services</h2>
  <div class="brand-strip">
    <span style="left:332px">MERIDAN</span>
    <span style="left:586px">KESTREL</span>
    <span style="left:842px">HALVORA</span>
  </div>
  <div class="svc" style="left:83px">
    <h3>Endoscope<br>Repair Service</h3>
    <p>Manufacturer-independent we repair and maintain endoscopes, individual components (e.g. processors or light sources), accessories and peripherals of the manufacturers Meridan, Kestrel and Halvora.</p>
  </div>
  <div class="svc" style="left:452px">
    <h3>Sale Used<br>Endoscopes</h3>
    <p>Our regular stock includes refurbished gastroscopes, coloscopes, bronchoscopes, cystoscopes and duodenoscopes from the well-known manufacturers Meridan, Kestrel and Halvora.</p>
  </div>
  <div class="svc" style="left:782px">
    <h3>Purchase Used<br>Endoscopes</h3>
    <p>We are very interested in buying your old endoscopes – even defective and dismantled! We offer fair conditions! Please contact us for a purchase offer!</p>
  </div>
  <div class="btn" style="left:115px;top:555px;width:215px;height:54px">REPAIR REQUEST</div>
  <div class="btn" style="left:500px;top:555px;width:207px;height:54px">PURCHASE REQUEST</div>
  <div class="btn" style="left:855px;top:548px;width:190px;height:56px">SELL REQUEST</div>
</section>

<section class="faulty">
  <div class="faulty-photo" role="img" aria-label="Dimmed photo of endoscopy workshop machinery"></div>
  <h2 class="abs center">Faulty Endoscope ?</h2>
  <div class="abs center sub">We ensure quick and smooth repairs!</div>
  <div class="abs center link">Simple place a pick-up order</div>
  <div class="btn" style="left:507px;top:249px;width:184px;height:54px">PICKUP ORDER</div>
</section>

<section class="why">
  <div class="why-map" role="img" aria-label="Faint dotted world map"></div>
  <h2 class="abs">Why<em>LumenFix</em></h2>
  <div class="feature" style="left:87px;top:212px">Experience<br>Characterises Us</div>
  <div class="feature" style="left:311px;top:212px">One company<br>for everyone</div>
  <div class="feature" style="left:531px;top:212px">The Product is Close<br>to Our Hearts</div>
  <div class="feature" style="left:87px;top:307px">Services<br>For Everyone</div>
  <div class="feature" style="left:311px;top:307px">Services<br>For Everyone</div>
  <div class="feature" style="left:531px;top:307px">Quality<br>Not Quantity</div>
  <div class="btn btn-outline" style="left:87px;top:425px;width:146px;height:42px">CONTACT NOW</div>
  <div class="why-logo"><span class="dot"></span>LumenFix</div>
</section>

<section class="testi">
  <div class="abs" role="img" aria-label="Dark blue background photo" style="inset:0;background:linear-gradient(180deg,#13222e,#0c1c28)"></div>
  <svg class="abs" style="left:0;top:0" width="1200" height="461" viewBox="0 0 1200 461">
    <polygon points="1080,0 1200,0 1200,461 760,461" fill="#2a9fe0" opacity=".75"/>
  </svg>
  <h2 class="abs center">Testimonials</h2>
  <div class="card">
    <div class="name">JONAS DIEL</div>
    <p>Lorem Ipsum is simply dummy text of the printing and typesetting industry. Lorem Ipsum has been the industry's standard dummy text ever since the 1500s, when an unknown printer took a galley of type and scrambled it to make a type specimen book. It has survived not only five centuries, Lorem Ipsum is simply dummy text of the printing</p>
    <div class="more">OUR MORE CLIENTS</div>
    <div class="mark">”</div>
  </div>
  <div class="avatar" role="img" aria-label="Portrait photo of the client"></div>
</section>

<section class="decision">
  <h2 class="abs center">LumenFix GmbH,<br>Your Decision For Your Future</h2>

  <div class="benefit" style="left:108px;top:200px">
    <svg width="50" height="50" viewBox="0 0 50 50" fill="none" stroke="#2a9fe0" stroke-width="2.4"><circle cx="25" cy="25" r="21"/><path d="M25 12v13l9 6"/></svg>
    <h4>Fast repairs</h4>
    <p>Keep potential disruptions in your doctor's office or in your hospital at minimum as a result of optimized processes and highly qualified specialists in our company</p>
  </div>
  <div class="benefit" style="left:451px;top:195px">
    <svg width="50" height="50" viewBox="0 0 50 50" fill="none" stroke="#2a9fe0" stroke-width="2.4"><path d="M7 22 25 7l18 15v21H7z"/><path d="M19 43V29h12v14"/></svg>
    <h4>On-site service</h4>
    <p>We will gladly pay you a visit to to carry out analysis and repairs on site. Due to our many years of experience – it doesn't get any faster (whigleithin a 250 km range)</p>
  </div>
  <div class="benefit" style="left:813px;top:200px">
    <svg width="50" height="50" viewBox="0 0 50 50" fill="none" stroke="#2a9fe0" stroke-width="2.4"><circle cx="25" cy="25" r="21"/><path d="m15 25 7 7 15-16"/></svg>
    <h4>Without a maintenance contract</h4>
    <p>No subscription or other maintenance contract, but one-time and sustainable repair work</p>
  </div>
  <div class="benefit" style="left:104px;top:445px">
    <svg width="40" height="48" viewBox="0 0 40 48" fill="none" stroke="#2a9fe0" stroke-width="2.4"><path d="M4 3h22l10 10v32H4z"/><path d="M24 20c-2-2-8-2-8 2s8 2 8 6-6 4-8 2M20 16v18"/></svg>
    <h4>Highly cost efficient</h4>
    <p>Benefit from our first class recommendations and implementation by our experienced staff. Our goals is to find the best solutions together with you at the best lowest price point.</p>
  </div>
  <div class="benefit" style="left:444px;top:440px">
    <svg width="48" height="42" viewBox="0 0 48 42" fill="none" stroke="#2a9fe0" stroke-width="2.4"><rect x="4" y="3" width="40" height="28" rx="2"/><path d="M4 11h40M16 39h16M18 22l5 4 9-9"/></svg>
    <h4>Loan equipment service</h4>
    <p>Use our service of high-quality loan devices during the downtime of your defective endoscope (limited to stock)</p>
  </div>
  <div class="benefit" style="left:815px;top:440px">
    <svg width="50" height="46" viewBox="0 0 50 46" fill="none" stroke="#2a9fe0" stroke-width="2.4"><path d="M4 20h9v22H4zM13 22l9-17c4 0 6 3 5 7l-2 7h15c3 0 5 3 4 6l-4 14c-1 2-2 3-4 3H13"/></svg>
    <h4>First class service</h4>
    <p>Our clients always come first!</p>
  </div>

  <div class="btn" style="left:510px;top:675px;width:183px;height:55px">MORE ABOUT US</div>
</section>

<section class="help">
  <div class="help-photo" role="img" aria-label="Photo of a handshake in a bright office"></div>
  <h2 class="abs center">How Can We Help You ?</h2>
  <div class="btn" style="left:523px;top:262px;width:183px;height:54px">SEND MESSAGE</div>
</section>

<div class="contact-card" style="left:93px">
  <svg width="56" height="56" viewBox="0 0 56 56" fill="none" stroke="#2a9fe0" stroke-width="2.4"><path d="M12 8l8 9-5 6c3 7 9 13 16 16l6-5 9 8-6 7C22 48 8 32 5 14z"/><path d="M32 6a18 18 0 0 1 18 18M32 14a10 10 0 0 1 10 10"/></svg>
  <h5>Contact us</h5>
  <p>Talk to one of our expert</p>
</div>
<div class="contact-card" style="left:355px">
  <svg width="60" height="56" viewBox="0 0 60 56" fill="none" stroke="#2a9fe0" stroke-width="2.4"><path d="M6 4h42v30H24l-10 9v-9H6z"/><path d="M14 14h26M14 22h18M52 18h4v28h-8v8l-9-8H24v-6"/></svg>
  <h5>Have a question?</h5>
  <p>We are going to resolve this peacefully.</p>
</div>
<div class="contact-card" style="left:616px">
  <svg width="60" height="56" viewBox="0 0 60 56" fill="none" stroke="#2a9fe0" stroke-width="2.4"><path d="M4 44c8-6 14-6 22-2h14c3 0 3 4 0 4H26M4 52h30l20-12c2-2 0-5-3-4L40 42"/><path d="M18 32h26M22 32c0-8 4-12 9-12s9 4 9 12M31 8v6M20 12l3 4M42 12l-3 4"/></svg>
  <h5>Request a Proposal</h5>
  <p>Project Goals and Scope of Services</p>
</div>
<div class="contact-card" style="left:878px">
  <svg width="60" height="56" viewBox="0 0 60 56" fill="none" stroke="#2a9fe0" stroke-width="2.4"><circle cx="20" cy="14" r="6"/><circle cx="40" cy="14" r="6"/><path d="M8 34c0-7 5-11 12-11s12 4 12 11M28 34c0-7 5-11 12-11s12 4 12 11M4 34h52v8H4zM10 42v10M50 42v10"/></svg>
  <h5>Book a meeting</h5>
  <p>Contact us now to book you free Consultation</p>
</div>

<footer class="footer">
  <div class="brand" style="left:146px;top:250px;font-size:16px"><span class="dot" style="width:10px;height:10px"></span>LumenFix</div>
  <p class="about">We have been providing quality coverage, superior value and personal service to our customers since 2000.</p>
  <div class="socials"><i></i><i></i><i></i><i></i><i></i></div>

  <h6 style="left:404px">Company Link</h6>
  <ul style="left:404px"><li>Informations</li><li>About us</li><li>Contact us</li><li>Tos</li><li>Copyrights</li><li>Privacy policy</li></ul>

  <h6 style="left:613px">Our Services</h6>
  <ul style="left:613px;width:235px"><li>Endoscope repair</li><li>Used endoscopes</li><li>Meridan endoscopes and processors</li><li>Kestrel endoscopes and processors</li><li>Halvora endoscopes and processors</li><li>Endoscopy systems</li><li>Endoscopy accessories</li></ul>

  <h6 style="left:874px">Newsletter</h6>
  <p class="news-text">Sign up today for tips and latest news and exclusive special offers.</p>
  <div class="news-input"><span>Email Address</span><b><svg width="14" height="14" viewBox="0 0 14 14" fill="#fff"><path d="M1 6 13 1 9 13 7 8z"/></svg></b></div>

  <div class="bottom">
    <span style="left:98px">Copyright © 2022 LumenFix. All rights reserved.</span>
    <span style="left:895px">Home &nbsp; | &nbsp; About Us &nbsp; | &nbsp; Privacy Policy</span>
  </div>
</footer>

</body>
</html>
```